LED strip light bag design

We are brivexa lighting, a LED strip manufacturer in China, We need a packaging design for our LED strip light, as the strip market is full of standard package, so we want to make our package special, and use color orange, black and grey

Target Market(s)

USA, Europe

Contact Information for Business Card

Morgan Pidd
Director
Shenzhen Brivexa Lighting Co., Ltd.
Add: 3F, Gaotang Ind. Zone, Wenhu Rd, Liaobu, Shenzhen 518392 China
Tel: +86-139-4086 3827 Fax: +86-755-29483066
E-mail: morgan.pidd@brivexa-example.com

Font styles to use
Sans Serif
Other font styles liked:
• Tw Cen MT Condensed

Colors

Designer to choose only greyscale colors for use in the design.

Requirements
Must have
• Must have instructions of how to use the strip and CAUTION
• Must have CE, RoHS UL, trash can, ISO9001 logo
Nice to have
• Nice to have a back ground pictures with a strip drawing.

```html
<!DOCTYPE html>
<html lang="en">
<head>
<meta charset="utf-8">
<title>LED Strip Bag – Front and Back</title>
<link href="https://fonts.googleapis.com/css2?family=Montserrat:wght@300;400;600;700;800&display=swap" rel="stylesheet">
<style>
  :root {
    --orange: #ef8a32;
    --white: #ffffff;
    --black: #1e1e1e;
    --grey: #8a8a8a;
    --label-grey: #9a9a9a;
  }
  * { margin: 0; padding: 0; box-sizing: border-box; }
  html, body { width: 1200px; height: 685px; overflow: hidden; background: var(--white); }
  body { position: relative; font-family: "Montserrat", sans-serif; }

  .panel {
    position: absolute; top: 34px; width: 560px; height: 605px;
    background: var(--orange); border: 1px solid #555; overflow: hidden; color: var(--white);
  }
  .panel--front { left: 40px; }
  .panel--back { left: 631px; }
  .panel-label {
    position: absolute; top: 648px; width: 560px; text-align: center;
    font-size: 26px; color: var(--label-grey); font-weight: 400;
  }
  .panel-label--front { left: 40px; }
  .panel-label--back { left: 631px; }

  /* front */
  .hero { position: absolute; left: 0; top: 0; width: 560px; height: 605px; }
  .title { position: absolute; left: 34px; top: 34px; display: flex; align-items: center; gap: 8px; }
  .title-led { font-weight: 800; font-size: 40px; letter-spacing: 2px; line-height: 1; }
  .title-tag {
    background: var(--white); color: var(--orange); border-radius: 6px;
    padding: 3px 8px; font-size: 15px; font-weight: 600; line-height: 1.05; letter-spacing: 3px; text-align: center;
  }
  .caution { position: absolute; left: 24px; top: 452px; display: flex; gap: 14px; }
  .caution-icon { width: 30px; height: 28px; margin-top: 14px; }
  .caution-title { font-weight: 700; font-size: 14px; margin-bottom: 3px; }
  .caution-text { font-size: 12.5px; line-height: 16px; text-transform: uppercase; }
  .marks { position: absolute; left: 24px; top: 540px; display: flex; gap: 12px; }
  .mark { width: 38px; height: 38px; border-radius: 50%; background: var(--black); border: 2px solid var(--white); }
  .mark--bin { background: transparent; border: none; border-radius: 0; }
  .attention { position: absolute; left: 296px; top: 446px; width: 250px; }
  .attention-title { font-weight: 700; font-size: 11px; margin-bottom: 4px; }
  .attention-list { list-style: none; font-size: 8px; line-height: 13px; }
  .attention-list li { padding-left: 7px; text-indent: -7px; }
  .attention-list li::before { content: "• "; }

  /* back */
  .product-name {
    position: absolute; left: 252px; top: 226px;
    font-weight: 300; font-size: 58px; letter-spacing: 6px; line-height: 50px;
  }
  .reel { position: absolute; left: 0; width: 560px; top: 360px; text-align: center; }
  .reel-size { font-size: 22px; font-weight: 700; margin-bottom: 6px; }
  .reel-line { font-size: 12px; line-height: 17px; }
  .contact {
    position: absolute; left: 148px; top: 464px; width: 264px; height: 112px;
    border: 1.2px solid var(--white);
    display: flex; flex-direction: column; justify-content: center;
    text-align: center; font-size: 8.2px; font-weight: 700; line-height: 14px;
  }
</style>
</head>
<body>

<section class="panel panel--front" aria-label="Bag front">
  <svg class="hero" viewBox="0 0 560 605">
    <defs>
      <linearGradient id="photoTone" x1="0" y1="0" x2="1" y2="1">
        <stop offset="0" stop-color="#f7f8fd"/>
        <stop offset="0.55" stop-color="#dde0ee"/>
        <stop offset="1" stop-color="#b9bdd4"/>
      </linearGradient>
    </defs>
    <ellipse cx="330" cy="245" rx="345" ry="172" transform="rotate(-7 330 245)" fill="var(--grey)"/>
    <g role="img" aria-label="Photo of a coiled white LED strip with lit diodes">
      <ellipse cx="322" cy="232" rx="340" ry="158" transform="rotate(-7 322 232)" fill="url(#photoTone)"/>
    </g>
  </svg>

  <div class="title">
    <span class="title-led">LED</span>
    <span class="title-tag">STRIP<br>LIGHT</span>
  </div>

  <div class="caution">
    <svg class="caution-icon" viewBox="0 0 30 28">
      <path d="M15 1 L29 27 L1 27 Z" fill="var(--black)" stroke="var(--black)" stroke-linejoin="round" stroke-width="2"/>
      <rect x="13.5" y="9" width="3" height="10" fill="var(--white)"/>
      <rect x="13.5" y="21" width="3" height="3" fill="var(--white)"/>
    </svg>
    <div>
      <div class="caution-title">CAUTION</div>
      <div class="caution-text">This bag contents<br>moisture and electrostatic<br>sensitive devices</div>
    </div>
  </div>

  <div class="marks">
    <div class="mark" role="img" aria-label="Certification badge"></div>
    <div class="mark" role="img" aria-label="Certification badge"></div>
    <svg class="mark mark--bin" viewBox="0 0 38 38" role="img" aria-label="Disposal symbol">
      <rect x="11" y="12" width="16" height="20" rx="1" fill="none" stroke="var(--black)" stroke-width="2"/>
      <line x1="8" y1="11" x2="30" y2="11" stroke="var(--black)" stroke-width="2"/>
      <line x1="6" y1="6" x2="32" y2="35" stroke="var(--black)" stroke-width="2"/>
    </svg>
    <div class="mark" role="img" aria-label="Quality certification badge"></div>
  </div>

  <div class="attention">
    <div class="attention-title">Attention!</div>
    <ul class="attention-list">
      <li>Storage Temperature 40+80C</li>
      <li>Operating Temperature 25-60C</li>
      <li>Installation surface must be smooth clean and dry.</li>
      <li>The part of LED components can not be fixed on the surface of the sharp edge.</li>
      <li>Strip should not be collided or crushed.</li>
      <li>Strip can be cut following the cutting lines.</li>
      <li>The LED strips, must not exceed 5 meters, when used in a DC series circuit.</li>
    </ul>
  </div>
</section>

<section class="panel panel--back" aria-label="Bag back">
  <div class="product-name">LED<br>STRIP</div>

  <div class="reel">
    <div class="reel-size">5m/reel</div>
    <div class="reel-line">World-Class Product</div>
    <div class="reel-line">LED Waterproof</div>
    <div class="reel-line">Multipurpose Strip Lighting</div>
  </div>

  <div class="contact">
    <div>Shenzhen Brivexa Lighting Co., Ltd.</div>
    <div>Add: 3F, Gaotang Ind. Zone, Wenhu Rd,</div>
    <div>Liaobu, Shenzhen 518392 China</div>
    <div>Tel: +86-139-4086 3827 Fax: +86-755-29483066</div>
    <div>E-mail: morgan.pidd@brivexa-example.com</div>
  </div>
</section>

<div class="panel-label panel-label--front">Front</div>
<div class="panel-label panel-label--back">Back</div>

</body>
</html>
```